Retro Label for old fashioned soda

We need a label for soda we are having private labeled for our retro, 1950's ice cream shop www.maplewhirlcones.com I don't want the label to look like something from 2017 with a retro feel, but more like an original (possibly kinda cheesy) label you'd see from the 1950's with some of the old catch lines like "tastes great", "invigorating" or "it is refreshing!" The prominent brand should be the name of our ice cream shop, The Maple Whirl. the soda is also pure cane sugar so it might be good to have that on somewhere

Label size is 2.4" wide by 4" tall. Here is an example of some retro labels from findoramap. I attached on file to this contest but there are more here: https://www.findoramap.net/search?q=retro+soda+label

The label will be the same for all the flavors with the exception of the flavor name changing somewhere on the label. These are the flavors

Root Beer
Orange
Black Cherry
Lemonade
Raspberry Lime -Rickey
White Birch Beer
Lemon Iced Tea
Vanilla Cream
Orange Cream
Sarsaparilla
Ginger Ale

Industry/Entity Type

Shop

Colors

Designer to choose colors to be used in the design.

Requirements
Must have
• retro feel. authentic old fashioned look

```html
<!DOCTYPE html>
<html lang="en">
<head>
<meta charset="utf-8">
<title>The Maple Whirl – Pure Cane Sugar Soda Labels</title>
<link rel="stylesheet" href="https://fonts.googleapis.com/css2?family=Righteous&family=Playfair+Display:ital,wght@1,700&display=swap">
<style>
  :root {
    --page: #ffffff;
    --teal: #3f6b78;
    --teal-dark: #335a66;
    --cream: #f1e6c8;
    --red: #d8262b;
    --header: #e9502c;
    --orange: #ec6f26;
    --orange-soft: #f2d35a;
    --cherry: #7c1a17;
    --cherry-soft: #eccb55;
    --lemon: #f4e94b;
    --lemon-soft: #f3e27a;
    --ink: #1d1a18;
  }
  * { margin: 0; padding: 0; box-sizing: border-box; }
  html, body { width: 1200px; height: 1200px; overflow: hidden; background: var(--page); }
  .board { position: relative; width: 1200px; height: 1200px; }
  .label { position: absolute; display: block; }
  .label--orange { left: 120px; top: 100px; width: 600px; height: 1000px; --accent: var(--orange); --accent-soft: var(--orange-soft); --flavor: var(--orange); }
  .label--cherry { left: 780px; top: 100px; width: 300px; height: 490px; --accent: var(--cherry); --accent-soft: var(--cherry-soft); --flavor: var(--cherry); }
  .label--lemon  { left: 780px; top: 610px; width: 300px; height: 490px; --accent: var(--lemon); --accent-soft: var(--lemon-soft); --flavor: var(--lemon); }

  .label__ground { fill: var(--teal); }
  .label__band { fill: var(--accent); opacity: .55; }
  .label__frame { fill: var(--cream); stroke: var(--accent); stroke-width: 18; }
  .label__frame-inner { fill: none; stroke: var(--accent); stroke-width: 5; }
  .label__art { fill: url(#artGlow); }
  .label--cherry .label__art { fill: url(#artGlowCherry); }
  .label--lemon .label__art { fill: url(#artGlowLemon); }
  .label__header { fill: var(--header); stroke: var(--red); stroke-width: 7; }
  .brand { font-family: "Righteous", sans-serif; fill: var(--cream); text-anchor: middle; }
  .claim { font-family: "Righteous", sans-serif; fill: var(--red); text-anchor: middle; font-size: 40px; }
  .flavor { font-family: "Righteous", sans-serif; fill: var(--flavor); text-anchor: middle; }
  .label--lemon .flavor { stroke: var(--ink); stroke-width: 2.5; paint-order: stroke; }
  .label--cherry .flavor { fill: var(--cherry); }
  .kind { font-family: "Righteous", sans-serif; fill: var(--teal); text-anchor: middle; font-size: 46px; letter-spacing: 26px; }
  .slogan { font-family: "Playfair Display", serif; font-style: italic; font-weight: 700; fill: var(--red); text-anchor: middle; font-size: 36px; text-decoration: underline; }
</style>
</head>
<body>
<main class="board">

  <svg width="0" height="0" style="position:absolute" aria-hidden="true">
    <defs>
      <radialGradient id="artGlow" cx="50%" cy="45%" r="60%">
        <stop offset="0" stop-color="#ef8a3a"/><stop offset=".45" stop-color="#f2d35a"/><stop offset="1" stop-color="#f1e6c8"/>
      </radialGradient>
      <radialGradient id="artGlowCherry" cx="50%" cy="45%" r="60%">
        <stop offset="0" stop-color="#9a2a1f"/><stop offset=".45" stop-color="#eccb55"/><stop offset="1" stop-color="#f1e6c8"/>
      </radialGradient>
      <radialGradient id="artGlowLemon" cx="50%" cy="45%" r="60%">
        <stop offset="0" stop-color="#f6ee6a"/><stop offset=".45" stop-color="#f3e27a"/><stop offset="1" stop-color="#f1e6c8"/>
      </radialGradient>
      <path id="cartouche" d="M120,30 H480 Q480,90 540,90 V380 Q590,420 590,500 Q590,580 540,620 V910 Q480,910 480,970 H120 Q120,910 60,910 V620 Q10,580 10,500 Q10,420 60,380 V90 Q120,90 120,30 Z"/>
      <path id="header" d="M170,110 H430 Q430,140 460,140 V330 H140 V140 Q170,140 170,110 Z"/>
    </defs>
  </svg>

  <!-- Orange -->
  <svg class="label label--orange" viewBox="0 0 600 1000" role="group" aria-label="Orange soda label">
    <rect class="label__ground" width="600" height="1000"/>
    <rect class="label__band" x="0" y="200" width="600" height="14"/>
    <rect class="label__band" x="0" y="790" width="600" height="14"/>
    <use href="#cartouche" class="label__frame"/>
    <path class="label__art" role="img" aria-label="Sunburst rays behind a soda fountain glass with two straws" d="M80,340 H520 V900 H80 Z"/>
    <use href="#cartouche" class="label__frame-inner" transform="translate(30,50) scale(.9)"/>
    <use href="#header" class="label__header"/>
    <text class="brand" x="300" y="205" font-size="58">The Maple</text>
    <text class="brand" x="300" y="280" font-size="70">Whirl</text>
    <text class="claim" x="300" y="460">PURE CANE SUGAR</text>
    <text class="flavor" x="300" y="560" font-size="108">ORANGE</text>
    <text class="kind" x="313" y="625">SODA</text>
    <text class="slogan" x="165" y="760">it is</text>
    <text class="slogan" x="165" y="800">refreshing!</text>
    <text class="slogan" x="440" y="760">tastes</text>
    <text class="slogan" x="440" y="800">great!</text>
  </svg>

  <!-- Black Cherry -->
  <svg class="label label--cherry" viewBox="0 0 600 1000" preserveAspectRatio="none" role="group" aria-label="Black cherry soda label">
    <rect class="label__ground" width="600" height="1000"/>
    <rect class="label__band" x="0" y="200" width="600" height="14"/>
    <rect class="label__band" x="0" y="790" width="600" height="14"/>
    <use href="#cartouche" class="label__frame"/>
    <path class="label__art" role="img" aria-label="Sunburst rays behind a soda fountain glass with two straws" d="M80,340 H520 V900 H80 Z"/>
    <use href="#cartouche" class="label__frame-inner" transform="translate(30,50) scale(.9)"/>
    <use href="#header" class="label__header"/>
    <text class="brand" x="300" y="205" font-size="58">The Maple</text>
    <text class="brand" x="300" y="280" font-size="70">Whirl</text>
    <text class="claim" x="300" y="430">PURE CANE SUGAR</text>
    <text class="flavor" x="300" y="500" font-size="66">BLACK</text>
    <text class="flavor" x="300" y="565" font-size="66">CHERRY</text>
    <text class="kind" x="313" y="625">SODA</text>
    <text class="slogan" x="165" y="760">it is</text>
    <text class="slogan" x="165" y="800">refreshing!</text>
    <text class="slogan" x="440" y="760">tastes</text>
    <text class="slogan" x="440" y="800">great!</text>
  </svg>

  <!-- Lemonade -->
  <svg class="label label--lemon" viewBox="0 0 600 1000" preserveAspectRatio="none" role="group" aria-label="Lemonade soda label">
    <rect class="label__ground" width="600" height="1000"/>
    <rect class="label__band" x="0" y="200" width="600" height="14"/>
    <rect class="label__band" x="0" y="790" width="600" height="14"/>
    <use href="#cartouche" class="label__frame"/>
    <path class="label__art" role="img" aria-label="Sunburst rays behind a soda fountain glass with two straws" d="M80,340 H520 V900 H80 Z"/>
    <use href="#cartouche" class="label__frame-inner" transform="translate(30,50) scale(.9)"/>
    <use href="#header" class="label__header"/>
    <text class="brand" x="300" y="205" font-size="58">The Maple</text>
    <text class="brand" x="300" y="280" font-size="70">Whirl</text>
    <text class="claim" x="300" y="450">PURE CANE SUGAR</text>
    <text class="flavor" x="300" y="535" font-size="76">LEMONADE</text>
    <text class="kind" x="313" y="610">SODA</text>
    <text class="slogan" x="165" y="760">it is</text>
    <text class="slogan" x="165" y="800">refreshing!</text>
    <text class="slogan" x="440" y="760">tastes</text>
    <text class="slogan" x="440" y="800">great!</text>
  </svg>

</main>
</body>
</html>
```